Landing page for a cyber security service provider called 'Lumen Grove'

The client is a new cyber security company in need of a website landing page at lumengrove.example.

Their visual identity is modern, playful, clean and uncluttered and represents innovation, connectivity and approachability.

The company logo is provided in black (attached) but the client is open to changing the colour to align with the new website design.

The landing page needs to contain:
- A call to action with a 'Get Started' button
-Links to blank 'How it works', 'Products', 'Pricing', 'About Us' and 'Contact Us' pages (that we'll fill out later)

Northmark Market(s)

Medium to large businesses who probably don't understand cyber / cyber security but need their business to be protected.

Industry/Entity Type

Cyber Security

Coding

Coded - Design and coding required

Number of Pages Required

1 page

Font styles to use
Sans Serif
Other font styles liked:
• Helvetica

Requirements
Nice to have
• Hero banner at the top of the landing page.
Should not have
• Should not look like a traditional cyber / cyber security design (eg no dark blue/ black, red/black colour combinations). Please no military styles (eg no shields, cannons, swords, guns)

```html
<!DOCTYPE html>
<html lang="en">
<head>
<meta charset="utf-8">
<title>Lumen Grove – Security Decisions</title>
<link href="https://fonts.googleapis.com/css2?family=Outfit:wght@400;500;600;700&family=Poppins:wght@400;500;600&display=swap" rel="stylesheet">
<style>
:root{
  --blue:#1a8ef0;
  --blue-deep:#1467d2;
  --blue-soft:#e9f2fd;
  --bg-tint:#f5f8fe;
  --ink:#16182a;
  --muted:#6f7688;
  --line:#e3e8f2;
  --cross:#e2434b;
  --white:#ffffff;
}
*{box-sizing:border-box;margin:0;padding:0}
html,body{width:1200px;height:4535px;overflow:hidden;background:var(--white)}
body{font-family:"Poppins",sans-serif;color:var(--ink);position:relative}
.page{position:relative;width:1200px;height:4535px;overflow:hidden}
.abs{position:absolute}
.backdrop{position:absolute;left:0;top:0}
h1,h2,h3{font-family:"Outfit",sans-serif;font-weight:500}
a{color:inherit;text-decoration:none}
.btn{position:absolute;display:flex;align-items:center;justify-content:center;border-radius:30px;font-family:"Poppins",sans-serif;font-weight:600;font-size:10px;letter-spacing:.4px;text-transform:uppercase}
.btn-solid{background:linear-gradient(90deg,var(--blue-deep),var(--blue) 60%,#3fb6f5);color:var(--white);box-shadow:0 8px 18px rgba(26,142,240,.3)}
.btn-ghost{border:1.5px solid var(--blue);color:var(--blue-deep);background:var(--white)}
.center{left:0;width:1200px;text-align:center}

/* header */
.brand{display:flex;align-items:center;gap:8px;font-family:"Outfit",sans-serif;font-weight:600;color:var(--blue)}
.brand .dot{width:14px;height:14px;border-radius:50%;background:var(--blue)}
.nav{left:350px;top:40px;display:flex;gap:23px;font-size:13px}
.nav a.active{color:var(--blue)}
.support{left:932px;top:32px;width:124px;height:36px;font-size:10px}

.hero-title{left:150px;top:150px;font-size:43px;line-height:53px;font-weight:500;letter-spacing:-.3px}
.hero-title span{color:var(--blue);font-weight:700}
.illus{border-radius:24px}
.down{left:567px;top:600px;width:66px;height:66px;border-radius:50%;background:var(--white);box-shadow:0 8px 24px rgba(40,90,170,.12);display:flex;align-items:center;justify-content:center}

.section-title{font-size:34px}
.lede{font-size:12.5px;line-height:30px;color:#3b4152}

/* services */
.svc{width:270px;text-align:center;top:941px;height:305px}
.svc .label{position:absolute;left:0;right:0;top:236px;font-size:12.5px;letter-spacing:.6px;color:var(--muted);font-weight:500}
.svc .pic{position:absolute;left:85px;top:50px;width:100px;height:100px;border-radius:22px}
.svc.active{background:var(--white);box-shadow:0 10px 30px rgba(40,90,170,.12);border-bottom:6px solid var(--blue)}
.svc.active .label{color:var(--blue)}
.svc .rule{position:absolute;left:55px;right:55px;top:196px;border-top:1px solid #b9d6f6}
.svc .rule i{position:absolute;left:50%;top:-6px;width:12px;height:12px;margin-left:-6px;border:2px solid var(--blue);border-radius:50%;background:var(--white)}

/* plans */
.plan{background:var(--white);box-shadow:0 12px 36px rgba(40,90,170,.12);overflow:hidden}
.plan .tier{position:absolute;left:0;right:0;text-align:center;font-size:12px;letter-spacing:1.2px;color:var(--muted)}
.plan .price{position:absolute;left:112px;font-family:"Outfit",sans-serif;font-size:29px;font-weight:600}
.plan .per{position:absolute;left:122px;font-size:9px;color:var(--muted)}
.plan .bar{position:absolute;width:26px;border-top:2px solid var(--blue)}
.plan ul{position:absolute;list-style:none;font-size:9.5px;color:#2c3142}
.plan li{height:22.4px;display:flex;align-items:center;gap:10px}
.plan li svg{flex:none}
.plan .wave{position:absolute;left:0;bottom:0}
.plan .details{position:absolute;height:30px;background:var(--white);border-radius:20px;color:var(--ink);font-size:9.5px;font-weight:600;letter-spacing:.3px;display:flex;align-items:center;justify-content:center;box-shadow:0 4px 14px rgba(0,0,0,.12)}

/* cta */
.ready{left:151px;top:2407px;width:905px;height:282px;background:var(--white);box-shadow:0 10px 40px rgba(40,90,170,.12)}

/* help diagram */
.node{position:absolute;width:54px;height:54px;margin:-27px 0 0 -27px;border-radius:50%;background:linear-gradient(135deg,#3fb6f5,var(--blue-deep));box-shadow:0 0 0 10px rgba(255,255,255,1),0 8px 26px rgba(26,142,240,.35);display:flex;align-items:center;justify-content:center}
.help-item h3{font-family:"Poppins",sans-serif;font-size:13px;font-weight:500;margin-bottom:8px}
.help-item p{font-size:9.5px;line-height:22px;color:#3b4152}
.right{text-align:right}

/* references */
.refs{top:3660px;left:225px;width:750px;display:flex;justify-content:space-between;align-items:center;font-family:"Outfit",sans-serif;font-size:21px;font-weight:600;color:#2a2f45}

/* footer */
.footer-col h4{font-family:"Poppins",sans-serif;font-size:13px;font-weight:500;margin-bottom:16px}
.footer-col a{display:block;font-size:11px;line-height:23.4px;color:#3b4152}
.footer-col a.active{color:var(--blue)}
.newsletter{left:834px;top:4300px;width:222px;height:42px;border:1px solid var(--line);border-radius:24px;display:flex;align-items:center;justify-content:space-between;padding:0 18px 0 20px;font-size:10px;color:#3b4152}
</style>
</head>
<body>
<div class="page">

<svg class="backdrop" width="1200" height="4535" viewBox="0 0 1200 4535" aria-hidden="true">
  <defs>
    <linearGradient id="tint" x1="0" y1="0" x2="0" y2="1">
      <stop offset="0" stop-color="#f1f5fd"/><stop offset="1" stop-color="#f7f9fe"/>
    </linearGradient>
  </defs>
  <path d="M0 0H1200V560C1000 620 820 640 600 620C360 600 160 520 0 470Z" fill="url(#tint)"/>
  <path d="M0 1660C120 1540 300 1470 600 1478C860 1485 1040 1560 1200 1640V2330C900 2370 500 2360 0 2300Z" fill="url(#tint)"/>
  <path d="M0 4040C200 3900 420 3880 640 3920C860 3960 1040 4020 1200 4000V4535H0Z" fill="#f6f9fe"/>
  <line x1="150" y1="4462" x2="1050" y2="4462" stroke="#e8ecf4"/>
</svg>

<!-- header -->
<header>
  <a class="abs brand" style="left:150px;top:36px;font-size:22px"><span class="dot"></span>Lumen Grove</a>
  <nav class="abs nav">
    <a class="active" href="#">Home</a><a href="#">How it works</a><a href="#">Products</a><a href="#">Pricing</a><a href="#">About Us</a><a href="#">Contact Us</a>
  </nav>
  <a class="btn btn-solid support" href="#">
    <svg width="14" height="14" viewBox="0 0 14 14" style="margin-right:7px"><path d="M2 8V7a5 5 0 0 1 10 0v1" fill="none" stroke="#fff" stroke-width="1.4"/><rect x="1.5" y="7.5" width="2.5" height="4" rx="1" fill="#fff"/><rect x="10" y="7.5" width="2.5" height="4" rx="1" fill="#fff"/></svg>Support</a>
</header>

<!-- hero -->
<section>
  <h1 class="abs hero-title">Make better-informed<br><span>Security Decisions<br>with Lumen Grove</span></h1>
  <a class="btn btn-solid" href="#" style="left:144px;top:349px;width:154px;height:46px;font-size:15px;text-transform:none;font-weight:500;letter-spacing:0">Get Started</a>
  <a class="btn btn-ghost" href="#" style="left:306px;top:352px;width:124px;height:42px;font-size:15px;text-transform:none;font-weight:500;letter-spacing:0;border-color:var(--line);color:var(--ink)">Contact Us</a>
  <div class="abs illus" role="img" aria-label="Isometric illustration of servers, a laptop and a person connected to a glowing network sphere" style="left:633px;top:114px;width:440px;height:386px;background:radial-gradient(circle at 40% 35%,#cfe5fb,#eaf3fd 55%,rgba(245,248,254,0) 75%)"></div>
  <div class="abs down"><svg width="16" height="26" viewBox="0 0 16 26"><path d="M8 1V24M2 18l6 6 6-6" fill="none" stroke="var(--blue)" stroke-width="1.6"/></svg></div>
</section>

<!-- services -->
<section>
  <h2 class="abs center section-title" style="top:752px">Our Services</h2>
  <p class="abs center lede" style="top:810px">Determine what applications and data can, and cannot be readily moved to a<br>cloud environment and what delivery models can be supported.</p>
  <div class="abs svc" style="left:48px"><div class="pic" role="img" aria-label="Cloud with gear illustration" style="background:linear-gradient(135deg,#8fd0fb,#1a8ef0)"></div><div class="label">MANAGED SERVICES</div></div>
  <div class="abs svc active" style="left:336px;width:269px"><div class="pic" role="img" aria-label="Secure laptop and server illustration" style="background:linear-gradient(135deg,#bfe2fc,#2a9bf2)"></div><div class="rule"><i></i></div><div class="label">MANAGED SECURITY</div></div>
  <div class="abs svc" style="left:620px"><div class="pic" role="img" aria-label="Monitor with chart and magnifier illustration" style="background:linear-gradient(135deg,#9ad6fb,#1677e0)"></div><div class="label">MANAGED MONITORING</div></div>
  <div class="abs svc" style="left:902px"><div class="pic" role="img" aria-label="Monitor with gears illustration" style="background:linear-gradient(135deg,#a2d9fb,#1a8ef0)"></div><div class="label">DEVOPS</div></div>
  <a class="btn btn-solid" href="#" style="left:526px;top:1318px;width:148px;height:42px">Try it for free</a>
</section>

<!-- plans -->
<section>
  <h2 class="abs center section-title" style="top:1610px">Managed Services Plans</h2>
  <p class="abs center" style="top:1670px;font-size:12.5px;color:var(--blue)">Choose what's best for you.</p>

  <article class="abs plan" style="left:243px;top:1763px;width:232px;height:502px">
    <div class="tier" style="top:32px">BASIC</div><div class="bar" style="left:113px;top:56px"></div>
    <div class="price" style="left:110px;top:68px;font-size:28px">$259</div><div class="per" style="left:135px;top:114px">Per month</div>
    <ul style="left:30px;top:152px">
      <li><svg width="9" height="8"><path d="M1 4l2.5 2.5L8 1" stroke="#29b36b" stroke-width="1.4" fill="none"/></svg>Incident response 24h</li>
      <li><svg width="9" height="8"><path d="M1 4l2.5 2.5L8 1" stroke="#29b36b" stroke-width="1.4" fill="none"/></svg>Governance</li>
      <li><svg width="9" height="8"><path d="M1 4l2.5 2.5L8 1" stroke="#29b36b" stroke-width="1.4" fill="none"/></svg>Monitoring</li>
      <li><svg width="9" height="8"><path d="M1 4l2.5 2.5L8 1" stroke="#29b36b" stroke-width="1.4" fill="none"/></svg>Identity &amp; Access Management</li>
      <li><svg width="9" height="8"><path d="M1 4l2.5 2.5L8 1" stroke="#29b36b" stroke-width="1.4" fill="none"/></svg>Backup</li>
      <li><svg width="9" height="8"><path d="M2 1l5 6M7 1L2 7" stroke="var(--cross)" stroke-width="1.3"/></svg>Performance Monitoring</li>
      <li><svg width="9" height="8"><path d="M2 1l5 6M7 1L2 7" stroke="var(--cross)" stroke-width="1.3"/></svg>Disaster Recovery</li>
      <li><svg width="9" height="8"><path d="M2 1l5 6M7 1L2 7" stroke="var(--cross)" stroke-width="1.3"/></svg>Cost &amp; Billing Management</li>
      <li><svg width="9" height="8"><path d="M2 1l5 6M7 1L2 7" stroke="var(--cross)" stroke-width="1.3"/></svg>Security Policies</li>
      <li><svg width="9" height="8"><path d="M2 1l5 6M7 1L2 7" stroke="var(--cross)" stroke-width="1.3"/></svg>Capacity management</li>
      <li><svg width="9" height="8"><path d="M2 1l5 6M7 1L2 7" stroke="var(--cross)" stroke-width="1.3"/></svg>Architecture</li>
      <li><svg width="9" height="8"><path d="M2 1l5 6M7 1L2 7" stroke="var(--cross)" stroke-width="1.3"/></svg>Automation</li>
    </ul>
    <svg class="wave" width="232" height="70"><path d="M0 22C60 0 120 45 232 18V70H0Z" fill="#bfeffb"/><path d="M0 40C70 20 140 60 232 34V70H0Z" fill="#3fd0f0"/><path d="M0 58C80 44 150 70 232 56V70H0Z" fill="#13b6e6"/></svg>
    <a class="details" href="#" style="left:60px;top:454px;width:112px">SEE DETAILS</a>
  </article>

  <article class="abs plan" style="left:727px;top:1763px;width:229px;height:502px">
    <div class="tier" style="top:32px">PREMIUM</div><div class="bar" style="left:102px;top:56px"></div>
    <div class="price" style="left:102px;top:68px;font-size:28px">$899</div><div class="per" style="left:102px;top:114px">Per month</div>
    <ul style="left:22px;top:152px">
      <li><svg width="9" height="8"><path d="M1 4l2.5 2.5L8 1" stroke="#29b36b" stroke-width="1.4" fill="none"/></svg>Incident response 24h</li>
      <li><svg width="9" height="8"><path d="M1 4l2.5 2.5L8 1" stroke="#29b36b" stroke-width="1.4" fill="none"/></svg>Governance</li>
      <li><svg width="9" height="8"><path d="M1 4l2.5 2.5L8 1" stroke="#29b36b" stroke-width="1.4" fill="none"/></svg>Monitoring</li>
      <li><svg width="9" height="8"><path d="M1 4l2.5 2.5L8 1" stroke="#29b36b" stroke-width="1.4" fill="none"/></svg>Identity &amp; Access Management</li>
      <li><svg width="9" height="8"><path d="M1 4l2.5 2.5L8 1" stroke="#29b36b" stroke-width="1.4" fill="none"/></svg>Backup</li>
      <li><svg width="9" height="8"><path d="M1 4l2.5 2.5L8 1" stroke="#29b36b" stroke-width="1.4" fill="none"/></svg>Performance Monitoring</li>
      <li><svg width="9" height="8"><path d="M1 4l2.5 2.5L8 1" stroke="#29b36b" stroke-width="1.4" fill="none"/></svg>Disaster Recovery</li>
      <li><svg width="9" height="8"><path d="M1 4l2.5 2.5L8 1" stroke="#29b36b" stroke-width="1.4" fill="none"/></svg>Cost &amp; Billing Management</li>
      <li><svg width="9" height="8"><path d="M1 4l2.5 2.5L8 1" stroke="#29b36b" stroke-width="1.4" fill="none"/></svg>Security Policies</li>
      <li><svg width="9" height="8"><path d="M1 4l2.5 2.5L8 1" stroke="#29b36b" stroke-width="1.4" fill="none"/></svg>Capacity management</li>
      <li><svg width="9" height="8"><path d="M1 4l2.5 2.5L8 1" stroke="#29b36b" stroke-width="1.4" fill="none"/></svg>Architecture</li>
      <li><svg width="9" height="8"><path d="M1 4l2.5 2.5L8 1" stroke="#29b36b" stroke-width="1.4" fill="none"/></svg>Automation</li>
    </ul>
    <svg class="wave" width="229" height="70"><path d="M0 18C90 44 150 0 229 22V70H0Z" fill="#c9dcf3"/><path d="M0 36C80 60 160 20 229 40V70H0Z" fill="#6d8fc4"/><path d="M0 56C80 68 160 44 229 58V70H0Z" fill="#24427c"/></svg>
    <a class="details" href="#" style="left:58px;top:454px;width:112px">SEE DETAILS</a>
  </article>

  <article class="abs plan" style="left:473px;top:1744px;width:254px;height:535px;z-index:2">
    <div class="tier" style="top:32px">STANDARD</div><div class="bar" style="left:116px;top:56px"></div>
    <div class="price" style="left:116px;top:76px;font-size:29px">$499</div><div class="per" style="left:118px;top:122px">Per month</div>
    <ul style="left:33px;top:171px">
      <li><svg width="9" height="8"><path d="M1 4l2.5 2.5L8 1" stroke="#29b36b" stroke-width="1.4" fill="none"/></svg>Incident response 24h</li>
      <li><svg width="9" height="8"><path d="M1 4l2.5 2.5L8 1" stroke="#29b36b" stroke-width="1.4" fill="none"/></svg>Governance</li>
      <li><svg width="9" height="8"><path d="M1 4l2.5 2.5L8 1" stroke="#29b36b" stroke-width="1.4" fill="none"/></svg>Monitoring</li>
      <li><svg width="9" height="8"><path d="M1 4l2.5 2.5L8 1" stroke="#29b36b" stroke-width="1.4" fill="none"/></svg>Identity &amp; Access Management</li>
      <li><svg width="9" height="8"><path d="M1 4l2.5 2.5L8 1" stroke="#29b36b" stroke-width="1.4" fill="none"/></svg>Backup</li>
      <li><svg width="9" height="8"><path d="M1 4l2.5 2.5L8 1" stroke="#29b36b" stroke-width="1.4" fill="none"/></svg>Performance Monitoring</li>
      <li><svg width="9" height="8"><path d="M1 4l2.5 2.5L8 1" stroke="#29b36b" stroke-width="1.4" fill="none"/></svg>Disaster Recovery</li>
      <li><svg width="9" height="8"><path d="M1 4l2.5 2.5L8 1" stroke="#29b36b" stroke-width="1.4" fill="none"/></svg>Cost &amp; Billing Management</li>
      <li><svg width="9" height="8"><path d="M2 1l5 6M7 1L2 7" stroke="var(--cross)" stroke-width="1.3"/></svg>Security Policies</li>
      <li><svg width="9" height="8"><path d="M2 1l5 6M7 1L2 7" stroke="var(--cross)" stroke-width="1.3"/></svg>Capacity management</li>
      <li><svg width="9" height="8"><path d="M2 1l5 6M7 1L2 7" stroke="var(--cross)" stroke-width="1.3"/></svg>Architecture</li>
      <li><svg width="9" height="8"><path d="M2 1l5 6M7 1L2 7" stroke="var(--cross)" stroke-width="1.3"/></svg>Automation</li>
    </ul>
    <svg class="wave" width="254" height="72"><path d="M0 20C70 0 150 46 254 16V72H0Z" fill="#c4e1fb"/><path d="M0 38C80 18 160 62 254 34V72H0Z" fill="#3f9bf0"/><path d="M0 58C90 46 160 72 254 54V72H0Z" fill="#1467d2"/></svg>
    <a class="details" href="#" style="left:70px;top:484px;width:114px">SEE DETAILS</a>
  </article>
</section>

<!-- call to action -->
<section class="abs ready">
  <h2 class="abs" style="left:0;width:905px;text-align:center;top:62px;font-size:33px;line-height:42px;font-weight:400">Are you ready?<br><span style="font-weight:500">Create an account, or contact us.</span></h2>
  <a class="btn btn-solid" href="#" style="left:290px;top:174px;width:186px;height:42px">Create your account</a>
  <a class="btn btn-ghost" href="#" style="left:491px;top:174px;width:124px;height:42px">Contact us</a>
</section>

<!-- help -->
<section>
  <h2 class="abs center section-title" style="top:2794px">We can also help you with</h2>
  <p class="abs center lede" style="top:2848px">Determine what applications and data can, and cannot be readily moved to a<br>cloud environment and what delivery models.</p>
  <svg class="abs" style="left:400px;top:2977px" width="400" height="400" aria-hidden="true">
    <circle cx="200" cy="200" r="167" fill="none" stroke="#cdd6e6" stroke-dasharray="3 5"/>
    <circle cx="200" cy="200" r="70" fill="#fff" style="filter:drop-shadow(0 8px 24px rgba(40,90,170,.16))"/>
  </svg>
  <div class="node" style="left:597px;top:3018px"><svg width="18" height="20"><rect x="2" y="1" width="14" height="18" rx="2" fill="none" stroke="#fff" stroke-width="1.6"/><path d="M6 6h6M6 10h6M6 14h4" stroke="#fff" stroke-width="1.4"/></svg></div>
  <div class="node" style="left:750px;top:3138px"><svg width="20" height="18"><rect x="1" y="2" width="18" height="4" rx="1" fill="#fff"/><rect x="1" y="8" width="18" height="4" rx="1" fill="#fff"/><rect x="1" y="14" width="18" height="3" rx="1" fill="#fff"/></svg></div>
  <div class="node" style="left:686px;top:3309px"><svg width="18" height="20"><rect x="3" y="9" width="12" height="9" rx="2" fill="none" stroke="#fff" stroke-width="1.6"/><path d="M6 9V6a3 3 0 0 1 6 0v3" fill="none" stroke="#fff" stroke-width="1.6"/></svg></div>
  <div class="node" style="left:503px;top:3309px"><svg width="20" height="20"><path d="M3 17L17 3M3 3l14 14" stroke="#fff" stroke-width="2" stroke-linecap="round"/></svg></div>
  <div class="node" style="left:438px;top:3138px"><svg width="20" height="20"><circle cx="10" cy="10" r="5.5" fill="none" stroke="#fff" stroke-width="2.4" stroke-dasharray="3 2"/><circle cx="10" cy="10" r="2" fill="#fff"/></svg></div>

  <div class="abs help-item" style="left:674px;top:2950px;width:300px"><h3>Assessment</h3><p>Determine what applications and data can, and cannot be<br>readily moved to a cloud environment.</p></div>
  <div class="abs help-item" style="left:812px;top:3107px;width:300px"><h3>Architectures</h3><p>Design Architectures references Network, Security, Identity<br>and Access Control, Hosting, Storage, Backup and DR,<br>Availability, Performance.</p></div>
  <div class="abs help-item" style="left:765px;top:3290px;width:320px"><h3>Security</h3><p>Design for your Cloud Security based on enterprise<br>standards and requirements for Security and Compliance to<br>keep data, applications and users secure.</p></div>
  <div class="abs help-item right" style="left:100px;top:3290px;width:338px"><h3>Build</h3><p>We help you automate and build/rebuild your designed<br>Infrastructures and applications with CI/CD pipelines.</p></div>
  <div class="abs help-item right" style="left:80px;top:3107px;width:292px"><h3>Automation / DevOps</h3><p>Continuous Integration, deployment and automation for<br>your infrastructures and applications.</p></div>
</section>

<!-- references -->
<section>
  <h2 class="abs center section-title" style="top:3516px">Our References</h2>
  <p class="abs center" style="top:3575px;font-size:11.5px;color:#3b4152">Lorem Ipsum is simply dummy text of the printing and typesetting industry.</p>
  <svg class="abs" style="left:106px;top:3670px" width="26" height="16" aria-hidden="true"><path d="M25 8H2M8 2L2 8l6 6" fill="none" stroke="#2a2f45" stroke-width="1.5"/></svg>
  <div class="abs refs"><span>Northmark</span><span>Pebblewood</span><span>Voltaro</span><span>Teleway</span><span>Swiftline</span></div>
  <svg class="abs" style="left:1070px;top:3670px" width="26" height="16" aria-hidden="true"><path d="M1 8H24M18 2l6 6-6 6" fill="none" stroke="#2a2f45" stroke-width="1.5"/></svg>
</section>

<!-- get started -->
<section>
  <div class="abs" style="left:537px;top:3807px;width:130px;height:130px;border-radius:50%;background:#fff;box-shadow:0 10px 30px rgba(40,90,170,.14)"></div>
  <h2 class="abs center section-title" style="top:3976px">Get Started With Lumen Grove</h2>
  <p class="abs center" style="top:4038px;font-size:13px;color:#3b4152">Cloud can be complex !! We help you Control it in an easy way.</p>
  <a class="btn btn-solid" href="#" style="left:459px;top:4087px;width:148px;height:42px">Try it for free</a>
  <a class="btn btn-ghost" href="#" style="left:616px;top:4087px;width:124px;height:42px;border-color:var(--line);color:var(--ink)">Contact us</a>
</section>

<!-- footer -->
<footer>
  <a class="abs brand" style="left:176px;top:4300px;font-size:24px"><span class="dot"></span>Lumen Grove</a>
  <div class="abs" style="left:152px;top:4376px;display:flex;align-items:center;gap:10px;font-size:13px;font-weight:500">Follow Us:
    <span style="width:28px;height:28px;border:1px solid #c6ccd8;border-radius:50%"></span><span style="font-size:11px;font-weight:400;color:#3b4152">Linkline</span></div>
  <div class="abs footer-col" style="left:482px;top:4246px"><h4>Company</h4>
    <a class="active" href="#">Home</a><a href="#">How it works</a><a href="#">Products</a><a href="#">Pricing</a><a href="#">About Us</a><a href="#">Contact Us</a></div>
  <div class="abs footer-col" style="left:644px;top:4248px"><h4>Services</h4>
    <a href="#">Managed Services</a><a href="#">Managed Security</a><a href="#">Managed Monitoring</a><a href="#">DevOps</a></div>
  <div class="abs footer-col" style="left:834px;top:4248px"><h4>Our Newsletter</h4></div>
  <div class="abs newsletter"><span>Join Our Newsletter</span><svg width="16" height="10"><path d="M1 5H14M10 1l4 4-4 4" fill="none" stroke="#7a8194" stroke-width="1.2"/></svg></div>
  <p class="abs center" style="top:4488px;font-size:11px;color:#3b4152">Copyright 2024 lumengrove.example</p>
</footer>

</div>
</body>
</html>
```